Basic Company webpage with the elements and colors of our Logo

Basic Home page with a few pages:
- Home,
- About US,
- Contact us
- Services

Target Market(s)

Business Customers (B2B)

Coding

Coded - Design and coding required

Number of Pages Required

5+ page

Requirements
Must have
• Professional, Clean, Simple High Tech, Contact should have a contact us dialog for sending messages to us
Nice to have
• Meet with us links for calendar access though MS Bookings

```html
<!DOCTYPE html>
<html lang="en">
<head>
<meta charset="utf-8">
<title>Nexora Tech Services Group — Website Pages</title>
<link href="https://fonts.googleapis.com/css2?family=Montserrat:wght@500;600;700;800&family=Open+Sans:wght@400;600&display=swap" rel="stylesheet">
<style>
:root{
  --navy:#0f3d61;
  --navy-d:#0a2b47;
  --orange:#f5a52a;
  --ink:#1d2a36;
  --muted:#5d6772;
  --bg:#d7d7d7;
  --line:#e3e7ec;
  --soft:#eef2f6;
  --white:#fff;
}
*{box-sizing:border-box}
html,body{margin:0;width:1200px;height:991px;overflow:hidden;background:var(--bg)}
.board{position:absolute;left:0;top:0;width:2100px;height:1736px;transform:scale(.5714);transform-origin:0 0}
.page{position:absolute;width:455px;background:var(--white);overflow:hidden;box-shadow:0 1px 4px rgba(0,0,0,.18);font-family:'Open Sans',sans-serif;color:var(--ink)}
.abs{position:absolute}
.h{font-family:'Montserrat',sans-serif}
p{margin:0}

/* header */
.logo{position:absolute;left:40px;top:11px;font:800 10.5px 'Montserrat',sans-serif;color:var(--navy);display:flex;align-items:center;gap:3px;letter-spacing:.2px}
.logo i{width:5px;height:5px;border-radius:50%;background:var(--orange);display:block}
.topbar{position:absolute;left:165px;top:0;width:290px;height:18px;background:var(--navy-d);clip-path:polygon(0 0,100% 0,100% 100%,14px 100%);color:#fff;font-size:5px;display:flex;align-items:center;gap:20px;padding-left:40px}
.topbar span{display:flex;align-items:center;gap:4px}
.topbar svg{width:8px;height:8px}
.nav{position:absolute;left:195px;top:24px;display:flex;gap:0;font:600 5.3px 'Montserrat',sans-serif;color:var(--ink)}
.nav span{width:62px}

/* hero */
.hero{position:absolute;left:0;top:36px;width:455px;background:var(--navy-d);overflow:hidden}
.hero-art{position:absolute;right:0;top:0;height:100%;width:270px}
.hero-curve{position:absolute;left:0;bottom:0;width:455px;height:90px}
.hero-text{position:absolute;left:42px;color:#fff}
.hero-text h2{margin:0;font:700 12px 'Montserrat',sans-serif}
.hero-text p{font-size:5px;line-height:1.75;margin-top:6px;width:175px;color:#e4ecf3}

/* titles */
.title{position:absolute;left:0;width:455px;text-align:center;font:700 11.5px 'Montserrat',sans-serif;color:var(--navy)}
.para{font-size:5px;line-height:1.9;color:var(--muted)}
.btn{position:absolute;font:700 5px 'Montserrat',sans-serif;display:flex;align-items:center;justify-content:center;border-radius:1px}
.btn.navy{background:var(--navy);color:#fff}
.btn.white{background:#fff;color:var(--navy)}
.btn.orange{background:var(--orange);color:#fff}
.ph{position:absolute}

/* footer */
.footer{position:absolute;left:0;width:455px;height:156px;background:#000;color:#fff}
.footer .flogo{position:absolute;left:42px;top:38px;font:800 11px 'Montserrat',sans-serif;color:#fff;display:flex;align-items:center;gap:3px}
.footer .flogo i{width:5px;height:5px;border-radius:50%;background:var(--orange);display:block}
.fcol{position:absolute;top:26px}
.fcol h4{margin:0 0 5px;font:600 7px 'Montserrat',sans-serif}
.fcol li{list-style:none;font-size:4.8px;line-height:11.5px}
.fcol li::before{content:"\2192";margin-right:4px;font-weight:700}
.fcol ul{margin:0;padding:0}
.fcontact div{display:flex;align-items:center;gap:6px;font-size:5px;height:22.5px}
.fcontact b{width:10px;height:10px;border-radius:50%;background:var(--navy);display:flex;align-items:center;justify-content:center}
.fcontact svg{width:5px;height:5px}
.footer hr{position:absolute;left:38px;top:126px;width:380px;margin:0;border:0;border-top:1px solid #555}
.footer .copy{position:absolute;left:0;width:455px;top:138px;text-align:center;font-size:4.8px}

/* inputs */
.field{position:absolute;background:#fff;border:1px solid var(--line);box-shadow:0 1px 3px rgba(0,0,0,.08);font-size:4.5px;color:#8a939c;padding:4px 6px}

/* cards */
.card{position:absolute;background:#fff;border-radius:3px;box-shadow:0 1px 4px rgba(0,0,0,.15)}
.icon-line{stroke:var(--navy);fill:none;stroke-width:1.3}
</style>
</head>
<body>
<svg width="0" height="0" style="position:absolute">
  <defs>
    <symbol id="i-phone" viewBox="0 0 24 24"><path d="M6.6 10.8a15 15 0 0 0 6.6 6.6l2.2-2.2a1 1 0 0 1 1-.25 11.4 11.4 0 0 0 3.6.6 1 1 0 0 1 1 1V20a1 1 0 0 1-1 1A17 17 0 0 1 3 4a1 1 0 0 1 1-1h3.5a1 1 0 0 1 1 1c0 1.25.2 2.45.57 3.57a1 1 0 0 1-.25 1z" fill="currentColor"/></symbol>
    <symbol id="i-mail" viewBox="0 0 24 24"><path d="M3 5h18v14H3z" fill="currentColor"/><path d="M3 6l9 7 9-7" stroke="#0a2b47" stroke-width="1.8" fill="none"/></symbol>
    <symbol id="i-pin" viewBox="0 0 24 24"><path d="M12 2a7 7 0 0 0-7 7c0 5 7 13 7 13s7-8 7-13a7 7 0 0 0-7-7zm0 9.5A2.5 2.5 0 1 1 12 6.5a2.5 2.5 0 0 1 0 5z" fill="currentColor"/></symbol>
  </defs>
</svg>

<div class="board">

<!-- ============ HOME ============ -->
<div class="page" style="left:71px;top:72px;height:1592px">
  <div class="logo"><i></i>NEXORA TECH</div>
  <div class="topbar"><span><svg style="color:#fff"><use href="#i-phone"/></svg>+1 555 010 0100</span><span><svg style="color:#fff"><use href="#i-mail"/></svg>info@nexoratech.example</span></div>
  <div class="nav"><span>HOME</span><span>ABOUT US</span><span>CONTACT US</span><span>SERVICES</span></div>

  <div class="hero" style="height:232px">
    <div class="hero-art" role="img" aria-label="Glowing digital globe made of network lines" style="background:radial-gradient(circle at 62% 45%,#5b3fd0 0%,#2a3c9e 25%,#0e2b5a 55%,#0a2b47 80%)"></div>
    <div class="hero-text" style="top:48px">
      <div class="h" style="font-weight:700;font-size:7px">WELCOME TO</div>
      <h2 style="font-size:17px;line-height:1.3;margin-top:6px">NEXORA TECH<br>SERVICES GROUP</h2>
      <p>Lorem ipsum dolor sit amet, consectetur adipiscing elit, sed do eiusmod tempor incididunt ut labore et dolore magna aliqua.</p>
    </div>
    <div class="btn white" style="left:42px;top:139px;width:58px;height:17px;border:1px solid #fff;font-size:4.6px">MEET WITH US</div>
    <svg class="hero-curve" viewBox="0 0 455 90" preserveAspectRatio="none"><path d="M0 22 Q227 112 455 22 L455 90 L0 90Z" fill="#fff"/><path d="M18 42 Q227 118 446 30 Q227 106 18 42Z" fill="var(--orange)"/></svg>
  </div>

  <div class="title" style="top:316px">WHY CHOOSE US</div>
  <p class="para abs" style="left:48px;top:344px;width:360px;text-align:center">Lorem ipsum dolor sit amet, consectetur adipiscing elit, sed do eiusmod tempor incididunt ut labore et dolore magna aliqua. Ut enim ad minim veniam, quis nostrud exercitation ullamco laboris nisi ut aliquip ex ea commodo consequat.</p>
  <div class="abs" style="left:60px;top:378px;width:340px;display:flex;justify-content:space-between;text-align:center;font:6.5px 'Times New Roman',serif">
    <div style="width:70px"><svg width="22" height="22" viewBox="0 0 24 24"><rect x="4" y="6" width="9" height="14" class="icon-line"/><rect x="13" y="10" width="7" height="10" class="icon-line"/><path d="M6 9h5M6 12h5M6 15h5" class="icon-line"/></svg><div style="margin-top:10px">Lorem ipsum</div></div>
    <div style="width:70px"><svg width="22" height="22" viewBox="0 0 24 24"><circle cx="12" cy="10" r="6" class="icon-line"/><path d="M9 10l2 2 4-4M6 20h12" class="icon-line"/></svg><div style="margin-top:10px">Lorem ipsum</div></div>
    <div style="width:70px"><svg width="22" height="22" viewBox="0 0 24 24"><circle cx="12" cy="7" r="3" class="icon-line"/><circle cx="7" cy="15" r="3" class="icon-line"/><circle cx="17" cy="15" r="3" class="icon-line"/></svg><div style="margin-top:10px">Lorem ipsum</div></div>
    <div style="width:70px"><svg width="22" height="22" viewBox="0 0 24 24"><circle cx="8" cy="10" r="3" class="icon-line"/><path d="M3 20c0-3 2-5 5-5s5 2 5 5M14 4h7v7h-7z" class="icon-line"/></svg><div style="margin-top:10px">Lorem ipsum</div></div>
  </div>

  <div class="abs" style="left:0;top:457px;width:455px;height:221px;background:var(--navy)">
    <div class="ph" role="img" aria-label="Two colleagues reviewing a tablet in an office, circular photo" style="left:46px;top:29px;width:162px;height:162px;border-radius:50%;border:3px solid #fff;background:linear-gradient(135deg,#dfe3e6,#a9b3bb 55%,#6f7a84)"></div>
    <div class="h" style="position:absolute;left:243px;top:38px;color:#fff;font-weight:700;font-size:11.5px">ABOUT US</div>
    <p class="para abs" style="left:227px;top:62px;width:185px;color:#dbe6ef">Sed ut perspiciatis unde omnis iste natus error sit voluptatem accusantium doloremque laudantium, totam rem aperiam, eaque ipsa quae ab illo inventore veritatis et quasi architecto beatae vitae dicta sunt explicabo. Nemo enim ipsam voluptatem quia voluptas sit aspernatur aut odit aut fugit, sed quia consequuntur magni dolores eos qui ratione voluptatem sequi nesciunt. Neque porro quisquam est, qui dolorem ipsum quia dolor sit amet, consectetur, adipisci velit, dolore magnam aliquam quaerat voluptatem.</p>
    <div class="btn white" style="left:227px;top:167px;width:50px;height:16px">Read More</div>
  </div>

  <div class="title" style="top:722px">OUR SERVICES</div>
  <svg class="abs" style="left:18px;top:806px" width="10" height="10" viewBox="0 0 10 10"><circle cx="5" cy="5" r="4.3" fill="none" stroke="#999" stroke-width=".6"/><path d="M6 3L4 5l2 2" stroke="#666" stroke-width=".7" fill="none"/></svg>
  <svg class="abs" style="left:427px;top:806px" width="10" height="10" viewBox="0 0 10 10"><circle cx="5" cy="5" r="4.3" fill="none" stroke="#999" stroke-width=".6"/><path d="M4 3l2 2-2 2" stroke="#666" stroke-width=".7" fill="none"/></svg>
  <div class="card" style="left:37px;top:758px;width:120px;height:124px;border-bottom:2px solid var(--navy)">
    <div role="img" aria-label="Businesswoman working at a desk with documents" style="height:92px;background:linear-gradient(160deg,#eef0f2,#b9c1c8 60%,#7d8893)"></div>
    <div class="h" style="text-align:center;font-size:5.5px;font-weight:600;margin-top:12px">Excepteur sint occaecat</div>
  </div>
  <div class="card" style="left:167px;top:758px;width:120px;height:186px;border:2px solid var(--orange);border-top:0;border-radius:0 0 4px 4px">
    <div role="img" aria-label="Smiling businesswoman shaking hands across a table" style="height:92px;background:linear-gradient(160deg,#e9ecee,#c4b7a6 55%,#6d7884)"></div>
    <div style="text-align:center;margin-top:6px">
      <div class="h" style="font-size:5.5px;font-weight:600;color:var(--orange)">Excepteur sint occaecat</div>
      <div style="font:4.6px/11.5px 'Times New Roman',serif;color:#333;margin-top:3px">Brand Development<br>Marketing<br>Ad Campaigns<br>Recruiting<br>Interviews and Onboarding</div>
    </div>
  </div>
  <div class="card" style="left:297px;top:758px;width:120px;height:124px;border-bottom:2px solid var(--navy)">
    <div role="img" aria-label="Team working at monitors in a dark office" style="height:92px;background:linear-gradient(160deg,#1c3554,#37577b 55%,#0e1f33)"></div>
    <div class="h" style="text-align:center;font-size:5.5px;font-weight:600;margin-top:12px">Excepteur sint occaecat</div>
  </div>

  <div class="abs" style="left:0;top:977px;width:455px;height:237px;background:var(--navy)">
    <div class="h" style="position:absolute;left:0;width:455px;text-align:center;top:38px;color:#fff;font-weight:700;font-size:11.5px">CLIENT &nbsp;TESTIMONIALS</div>
    <svg class="abs" style="left:16px;top:135px" width="14" height="14" viewBox="0 0 14 14"><circle cx="7" cy="7" r="6.5" fill="#fff"/><path d="M8 4.5L5.5 7 8 9.5" stroke="var(--navy)" stroke-width="1" fill="none"/></svg>
    <svg class="abs" style="left:428px;top:135px" width="14" height="14" viewBox="0 0 14 14"><circle cx="7" cy="7" r="6.5" fill="#fff"/><path d="M6 4.5L8.5 7 6 9.5" stroke="var(--navy)" stroke-width="1" fill="none"/></svg>
  </div>
  <div class="abs" style="left:42px;top:1051px;width:117px;height:125px;border:1px solid #fff;border-radius:3px;color:#fff;padding:9px">
    <div style="color:var(--orange);font-size:6px;letter-spacing:.5px">★★★★★</div>
    <p style="font-size:4.7px;line-height:1.9;margin-top:3px">Lorem ipsum dolor sit amet, consectetur adipiscing elit, sed do eiusmod tempor incididunt ut labore et dolore magna aliqua ut enim ad minim veniam, quis nostrud exercitation ullamco.</p>
    <div style="position:absolute;left:9px;bottom:9px;display:flex;align-items:center;gap:6px"><b role="img" aria-label="Client portrait" style="width:20px;height:20px;border-radius:50%;background:#c9ced3;display:block"></b><div><div class="h" style="font-size:5.5px;font-weight:700">Glen Ashworth</div><div style="font-size:4.5px;color:#d3dde6">Florida, United States</div></div></div>
  </div>
  <div class="abs" style="left:169px;top:1051px;width:117px;height:125px;border:1px solid #fff;border-radius:3px;color:#fff;padding:9px">
    <div style="color:var(--orange);font-size:6px;letter-spacing:.5px">★★★★★</div>
    <p style="font-size:4.7px;line-height:1.9;margin-top:3px">Lorem ipsum dolor sit amet, consectetur adipiscing elit, sed do eiusmod tempor incididunt ut labore et dolore magna aliqua ut enim ad minim veniam, quis nostrud exercitation ullamco.</p>
    <div style="position:absolute;left:9px;bottom:9px;display:flex;align-items:center;gap:6px"><b role="img" aria-label="Client portrait" style="width:20px;height:20px;border-radius:50%;background:#c9ced3;display:block"></b><div><div class="h" style="font-size:5.5px;font-weight:700">Dana Reyes</div><div style="font-size:4.5px;color:#d3dde6">Florida, United States</div></div></div>
  </div>
  <div class="abs" style="left:296px;top:1051px;width:117px;height:125px;border:1px solid #fff;border-radius:3px;color:#fff;padding:9px">
    <div style="color:var(--orange);font-size:6px;letter-spacing:.5px">★★★★★</div>
    <p style="font-size:4.7px;line-height:1.9;margin-top:3px">Lorem ipsum dolor sit amet, consectetur adipiscing elit, sed do eiusmod tempor incididunt ut labore et dolore magna aliqua ut enim ad minim veniam, quis nostrud exercitation ullamco.</p>
    <div style="position:absolute;left:9px;bottom:9px;display:flex;align-items:center;gap:6px"><b role="img" aria-label="Client portrait" style="width:20px;height:20px;border-radius:50%;background:#c9ced3;display:block"></b><div><div class="h" style="font-size:5.5px;font-weight:700">Owen Pratt</div><div style="font-size:4.5px;color:#d3dde6">Florida, United States</div></div></div>
  </div>

  <div class="title" style="top:1260px">CONTACT US</div>
  <div class="field" style="left:68px;top:1290px;width:157px;height:18px">Name</div>
  <div class="field" style="left:230px;top:1290px;width:157px;height:18px">Email</div>
  <div class="field" style="left:68px;top:1314px;width:157px;height:18px">Phone Number</div>
  <div class="field" style="left:230px;top:1314px;width:157px;height:18px">Subject</div>
  <div class="field" style="left:68px;top:1338px;width:319px;height:34px">Message</div>
  <div class="btn navy" style="left:201px;top:1380px;width:52px;height:18px">Submit</div>

  <div class="footer" style="top:1436px">
    <div class="flogo"><i></i>NEXORA TECH</div>
    <div class="fcol" style="left:168px"><h4>Quick Links</h4><ul><li>Home</li><li>About Us</li><li>Services</li><li>Contact Us</li></ul></div>
    <div class="fcol" style="left:237px"><h4>Other Links</h4><ul><li>FAQ</li><li>Terms of Use</li><li>Privacy Policy</li><li>Support Links</li><li>Conditions</li></ul></div>
    <div class="fcol fcontact" style="left:321px"><h4>Contact Us</h4><div><b><svg style="color:#fff"><use href="#i-pin"/></svg></b>Company Name,United State.</div><div><b><svg style="color:#fff"><use href="#i-mail"/></svg></b>info@companyname.com</div><div><b><svg style="color:#fff"><use href="#i-phone"/></svg></b>+1 555 010 0100</div></div>
    <hr><div class="copy">Copyrights@2025 Nexora Tech Services Group.All Rights Reserved</div>
  </div>
</div>

<!-- ============ ABOUT ============ -->
<div class="page" style="left:572px;top:72px;height:1268px">
  <div class="logo"><i></i>NEXORA TECH</div>
  <div class="topbar"><span><svg style="color:#fff"><use href="#i-phone"/></svg>+1 555 010 0100</span><span><svg style="color:#fff"><use href="#i-mail"/></svg>info@nexoratech.example</span></div>
  <div class="nav"><span>HOME</span><span>ABOUT US</span><span>CONTACT US</span><span>SERVICES</span></div>
  <div class="hero" style="height:205px">
    <div class="hero-art" role="img" aria-label="Hand holding a glowing globe surrounded by technology icons" style="background:radial-gradient(circle at 45% 40%,#d98a3a 0%,#3c4f6e 25%,#1d2b3e 55%,#111c2a 85%)"></div>
    <div class="hero-text" style="top:50px"><h2 style="font-size:13px">ABOUT US</h2><p>Lorem ipsum dolor sit amet, consectetur adipiscing elit, sed do eiusmod tempor incididunt ut labore et dolore magna aliqua. Ut enim ad minim veniam, quis nostrud exercitation ullamco laboris nisi ut aliquip ex ea commodo consequat.</p></div>
    <svg class="hero-curve" viewBox="0 0 455 90" preserveAspectRatio="none"><path d="M0 22 Q227 112 455 22 L455 90 L0 90Z" fill="#fff"/><path d="M18 42 Q227 118 446 30 Q227 106 18 42Z" fill="var(--orange)"/></svg>
  </div>

  <div class="abs" style="left:48px;top:292px;width:151px;height:140px;background:var(--soft)"></div>
  <div class="ph" role="img" aria-label="Business team meeting around a laptop in a bright office" style="left:62px;top:278px;width:151px;height:139px;background:linear-gradient(150deg,#e8eaec,#b8bec4 55%,#6f757c)"></div>
  <div class="h abs" style="left:250px;top:286px;font-weight:600;font-size:11.5px;color:var(--navy)">Who We Are</div>
  <p class="para abs" style="left:242px;top:314px;width:172px;color:#444"><b>Lorem ipsum dolor sit amet, consectetur adipiscing elit, sed do eiusmod tempor incididunt ut labore et dolore aliqua.</b> Ut enim ad minim veniam, quis nostrud exercitation ullamco laboris nisi ut aliquip ex ea commodo consequat. Duis aute irure dolor in reprehenderit in voluptate velit esse cillum dolore eu fugiat nulla pariatur. Excepteur sint occaecat cupidatat non proident, sunt in culpa qui officia deserunt mollit anim id perspiciatis unde omnis iste natus error sit voluptatem vitae dicta sunt explicabo. Nemo fugit, sed quia consequuntur magni dolores eos qui ratione voluptatem sequi nesciunt.</p>

  <div class="abs" style="left:0;top:470px;width:455px;height:273px;background:var(--navy);color:#fff">
    <div class="h" style="position:absolute;left:0;width:455px;text-align:center;top:40px;font-weight:600;font-size:11.5px">What We Do</div>
    <p style="position:absolute;left:60px;width:335px;top:70px;text-align:center;font-size:5px;line-height:2">We provide a wide range of IT Managed Services designed to ensure your technology infrastructure runs smoothly.<br>Our services include, but are not limited to:</p>
    <div style="position:absolute;left:42px;top:110px;width:175px">
      <div style="display:flex;gap:7px;height:46px"><b style="flex:none;width:27px;height:27px;border-radius:50%;background:#fff;display:block;margin-top:4px"></b><div><div class="h" style="font-size:5.8px;font-weight:600">Network Monitoring and Management:</div><p style="font-size:4.8px;line-height:1.9;margin-top:3px;color:#dbe6ef">Lorem ipsum dolor sit amet, consectetur adipiscing elit, sed do eiusmod tempor dolore magna aliqua.</p></div></div>
      <div style="display:flex;gap:7px;height:46px"><b style="flex:none;width:27px;height:27px;border-radius:50%;background:#fff;display:block;margin-top:4px"></b><div><div class="h" style="font-size:5.8px;font-weight:600">Cybersecurity Solutions:</div><p style="font-size:4.8px;line-height:1.9;margin-top:3px;color:#dbe6ef">Lorem ipsum dolor sit amet, consectetur adipiscing elit, sed do eiusmod tempor dolore magna aliqua.</p></div></div>
      <div style="display:flex;gap:7px;height:46px"><b style="flex:none;width:27px;height:27px;border-radius:50%;background:#fff;display:block;margin-top:4px"></b><div><div class="h" style="font-size:5.8px;font-weight:600">Cloud Solutions</div><p style="font-size:4.8px;line-height:1.9;margin-top:3px;color:#dbe6ef">Lorem ipsum dolor sit amet, consectetur adipiscing elit, sed do eiusmod tempor dolore magna aliqua.</p></div></div>
    </div>
    <div style="position:absolute;left:257px;top:120px;width:156px;height:120px;background:#3a5f80"></div>
    <div role="img" aria-label="Two colleagues discussing work on a tablet" style="position:absolute;left:247px;top:110px;width:156px;height:120px;background:linear-gradient(150deg,#dde1e4,#a9b0b6 55%,#5d6670)"></div>
  </div>

  <div class="h abs" style="left:0;width:455px;text-align:center;top:786px;font-weight:600;font-size:11.5px;color:var(--navy)">Why Choose Us?</div>
  <div class="card" style="left:42px;top:820px;width:117px;height:122px;padding:10px">
    <svg width="18" height="18" viewBox="0 0 24 24"><circle cx="12" cy="12" r="4" class="icon-line"/><circle cx="12" cy="12" r="8" class="icon-line" stroke-dasharray="3 2"/></svg>
    <div class="h" style="font-size:6.5px;font-weight:600;margin-top:3px">Expert Team</div>
    <p class="para" style="margin-top:3px">Lorem ipsum dolor sit amet, eiusmod tempor incididunt ut labore et dolore magna aliqua. Ut enim ad minim ullamco laboris nisi ut aliquip ex ea commodo consequat.</p>
  </div>
  <div class="card" style="left:170px;top:820px;width:117px;height:122px;padding:10px">
    <svg width="18" height="18" viewBox="0 0 24 24"><path d="M12 3l7 3v5c0 5-3 8-7 10-4-2-7-5-7-10V6z" fill="var(--orange)"/><path d="M9 12l2 2 4-4" stroke="#fff" stroke-width="1.5" fill="none"/></svg>
    <div class="h" style="font-size:6.5px;font-weight:600;margin-top:3px">Reliability</div>
    <p class="para" style="margin-top:3px">Lorem ipsum dolor sit amet, eiusmod tempor incididunt ut labore et dolore magna aliqua. Ut enim ad minim ullamco laboris nisi ut aliquip ex ea commodo consequat.</p>
  </div>
  <div class="card" style="left:297px;top:820px;width:117px;height:122px;padding:10px">
    <svg width="18" height="18" viewBox="0 0 24 24"><rect x="5" y="5" width="14" height="14" fill="var(--navy)"/><path d="M9 15l6-6M11 9h4v4" stroke="#fff" stroke-width="1.5" fill="none"/></svg>
    <div class="h" style="font-size:6.5px;font-weight:600;margin-top:3px">Expert Team</div>
    <p class="para" style="margin-top:3px">Lorem ipsum dolor sit amet, eiusmod tempor incididunt ut labore et dolore magna aliqua. Ut enim ad minim ullamco laboris nisi ut aliquip ex ea commodo consequat.</p>
  </div>

  <div class="abs" style="left:0;top:980px;width:455px;height:132px;background:var(--soft)">
    <div class="h" style="position:absolute;left:0;width:455px;text-align:center;top:40px;font-weight:600;font-size:11.5px;color:var(--navy)">Let Us Help You Thrive</div>
    <p class="para" style="position:absolute;left:50px;width:355px;top:70px;text-align:center;color:#444">Lorem ipsum dolor sit amet, consectetur adipiscing elit, sed do eiusmod tempor incididunt ut labore et dolore magna aliqua. Ut enim ad minim veniam, quis nostrud exercitation ullamco laboris nisi ut aliquip ex ea commodo consequat. Duis aute irure dolor in reprehenderit in voluptate velit esse cillum dolore eu fugiat nulla pariatur.</p>
  </div>

  <div class="footer" style="top:1112px">
    <div class="flogo"><i></i>NEXORA TECH</div>
    <div class="fcol" style="left:168px"><h4>Quick Links</h4><ul><li>Home</li><li>About Us</li><li>Services</li><li>Contact Us</li></ul></div>
    <div class="fcol" style="left:237px"><h4>Other Links</h4><ul><li>FAQ</li><li>Terms of Use</li><li>Privacy Policy</li><li>Support Links</li><li>Conditions</li></ul></div>
    <div class="fcol fcontact" style="left:321px"><h4>Contact Us</h4><div><b><svg style="color:#fff"><use href="#i-pin"/></svg></b>Company Name,United State.</div><div><b><svg style="color:#fff"><use href="#i-mail"/></svg></b>info@companyname.com</div><div><b><svg style="color:#fff"><use href="#i-phone"/></svg></b>+1 555 010 0100</div></div>
    <hr><div class="copy">Copyrights@2025 Nexora Tech Services Group.All Rights Reserved</div>
  </div>
</div>

<!-- ============ SERVICES ============ -->
<div class="page" style="left:1074px;top:72px;height:974px">
  <div class="logo"><i></i>NEXORA TECH</div>
  <div class="topbar"><span><svg style="color:#fff"><use href="#i-phone"/></svg>+1 555 010 0100</span><span><svg style="color:#fff"><use href="#i-mail"/></svg>info@nexoratech.example</span></div>
  <div class="nav"><span>HOME</span><span>ABOUT US</span><span>CONTACT US</span><span>SERVICES</span></div>
  <div class="hero" style="height:205px">
    <div class="hero-art" role="img" aria-label="Robot touching a glowing holographic interface" style="background:radial-gradient(circle at 55% 55%,#c9304a 0%,#2d3a9c 30%,#0f2a66 60%,#0a2b47 85%)"></div>
    <div class="hero-text" style="top:50px"><h2 style="font-size:13px">SERVICES</h2><p>Lorem ipsum dolor sit amet, consectetur adipiscing elit, sed do eiusmod tempor incididunt ut labore et dolore magna aliqua. Ut enim ad minim veniam, quis nostrud exercitation ullamco laboris nisi ut aliquip ex ea commodo consequat.</p></div>
    <svg class="hero-curve" viewBox="0 0 455 90" preserveAspectRatio="none"><path d="M0 22 Q227 112 455 22 L455 90 L0 90Z" fill="#fff"/><path d="M18 42 Q227 118 446 30 Q227 106 18 42Z" fill="var(--orange)"/></svg>
  </div>

  <svg class="abs" style="left:0;top:0" width="455" height="974"><path d="M114 408V431H310V455M318 583V617H122V642" stroke="#9aa3ab" stroke-width=".8" fill="none"/></svg>

  <div class="abs" style="left:52px;top:284px;width:155px;height:124px;background:var(--soft)"></div>
  <div class="ph" role="img" aria-label="Two IT engineers with a laptop in a server room" style="left:62px;top:274px;width:155px;height:123px;background:linear-gradient(150deg,#2b4d74,#5a7ea3 50%,#17304f)"></div>
  <div class="h abs" style="left:240px;top:273px;font-weight:600;font-size:10px;line-height:1.5;color:var(--ink)">IT CONSULTING &amp; STRATEGIC<br>PLANNING</div>
  <p class="para abs" style="left:240px;top:308px;width:172px">Lorem ipsum dolor sit amet, consectetur adipiscing elit, sed do eiusmod tempor incididunt ut labore et dolore magna aliqua. Ut enim ad minim veniam, quis nostrud exercitation ullamco laboris nisi ut aliquip ex ea commodo consequat. Duis aute irure dolor in reprehenderit in voluptate velit esse cillum dolore eu fugiat nulla pariatur.</p>
  <div class="btn navy" style="left:240px;top:388px;width:58px;height:17px">READ MORE</div>

  <div class="h abs" style="left:53px;top:459px;font-weight:600;font-size:10px;line-height:1.5;color:var(--ink)">DATA BACKUP &amp; DISASTER<br>RECOVERY</div>
  <p class="para abs" style="left:53px;top:494px;width:172px">Lorem ipsum dolor sit amet, consectetur adipiscing elit, sed do eiusmod tempor incididunt ut labore et dolore magna aliqua. Ut enim ad minim veniam, quis nostrud exercitation ullamco laboris nisi ut aliquip ex ea commodo consequat. Duis aute irure dolor in reprehenderit in voluptate velit esse cillum dolore eu fugiat nulla pariatur.</p>
  <div class="btn orange" style="left:53px;top:574px;width:58px;height:17px">READ MORE</div>
  <div class="abs" style="left:241px;top:470px;width:155px;height:124px;background:#fde8c6"></div>
  <div class="ph" role="img" aria-label="Server room corridor with a glowing cloud symbol" style="left:251px;top:460px;width:155px;height:123px;background:radial-gradient(circle at 50% 50%,#2fb4e6 0%,#1a4d86 35%,#0c1f3d 80%)"></div>

  <div class="abs" style="left:52px;top:654px;width:155px;height:124px;background:var(--soft)"></div>
  <div class="ph" role="img" aria-label="Laptop with glowing blue data streams" style="left:62px;top:644px;width:155px;height:123px;background:linear-gradient(150deg,#0c2f6e,#2a6fd0 50%,#081b3c)"></div>
  <div class="h abs" style="left:240px;top:643px;font-weight:600;font-size:10px;line-height:1.5;color:var(--ink)">MANAGED IT SECURITY<br>SERVICES</div>
  <p class="para abs" style="left:240px;top:678px;width:172px">Lorem ipsum dolor sit amet, consectetur adipiscing elit, sed do eiusmod tempor incididunt ut labore et dolore magna aliqua. Ut enim ad minim veniam, quis nostrud exercitation ullamco laboris nisi ut aliquip ex ea commodo consequat. Duis aute irure dolor in reprehenderit in voluptate velit esse cillum dolore eu fugiat nulla pariatur.</p>
  <div class="btn navy" style="left:240px;top:758px;width:58px;height:17px">READ MORE</div>

  <div class="footer" style="top:818px">
    <div class="flogo"><i></i>NEXORA TECH</div>
    <div class="fcol" style="left:168px"><h4>Quick Links</h4><ul><li>Home</li><li>About Us</li><li>Services</li><li>Contact Us</li></ul></div>
    <div class="fcol" style="left:237px"><h4>Other Links</h4><ul><li>FAQ</li><li>Terms of Use</li><li>Privacy Policy</li><li>Support Links</li><li>Conditions</li></ul></div>
    <div class="fcol fcontact" style="left:321px"><h4>Contact Us</h4><div><b><svg style="color:#fff"><use href="#i-pin"/></svg></b>Company Name,United State.</div><div><b><svg style="color:#fff"><use href="#i-mail"/></svg></b>info@companyname.com</div><div><b><svg style="color:#fff"><use href="#i-phone"/></svg></b>+1 555 010 0100</div></div>
    <hr><div class="copy">Copyrights@2025 Nexora Tech Services Group.All Rights Reserved</div>
  </div>
</div>

<!-- ============ CONTACT ============ -->
<div class="page" style="left:1575px;top:72px;height:633px">
  <div class="logo"><i></i>NEXORA TECH</div>
  <div class="topbar"><span><svg style="color:#fff"><use href="#i-phone"/></svg>+1 555 010 0100</span><span><svg style="color:#fff"><use href="#i-mail"/></svg>info@nexoratech.example</span></div>
  <div class="nav"><span>HOME</span><span>ABOUT US</span><span>CONTACT US</span><span>SERVICES</span></div>
  <div class="hero" style="height:205px">
    <div class="hero-art" role="img" aria-label="Two engineers with a laptop in a data center" style="width:455px;background:linear-gradient(90deg,#0e2540 0%,#1f3f63 40%,#3b5d80 70%,#1a3250)"></div>
    <div class="hero-text" style="top:50px"><h2 style="font-size:13px">CONTACT US</h2><p>Lorem ipsum dolor sit amet, consectetur adipiscing elit, sed do eiusmod tempor incididunt ut labore et dolore magna aliqua. Ut enim ad minim veniam, quis nostrud exercitation ullamco laboris nisi ut aliquip ex ea commodo consequat.</p></div>
    <svg class="hero-curve" viewBox="0 0 455 90" preserveAspectRatio="none"><path d="M0 22 Q227 112 455 22 L455 90 L0 90Z" fill="#fff"/><path d="M18 42 Q227 118 446 30 Q227 106 18 42Z" fill="var(--orange)"/></svg>
  </div>

  <div class="h abs" style="left:0;width:455px;text-align:center;top:270px;font-weight:700;font-size:11.5px;color:var(--ink)">CONTACT US</div>
  <p class="para abs" style="left:65px;width:325px;top:293px;text-align:center;color:#444">Duis aute irure dolor in reprehenderit in voluptate velit esse cillum dolore eu fugiat nulla pariatur. Excepteur sint occaecat cupidatat non proident, sunt in culpa qui officia deserunt mollit anim id est laborum.</p>

  <div class="abs" style="left:43px;top:330px;width:140px">
    <div style="display:flex;gap:10px;height:39px"><b style="flex:none;width:31px;height:31px;border-radius:50%;background:var(--navy);display:flex;align-items:center;justify-content:center"><svg width="13" height="13" style="color:#fff"><use href="#i-pin"/></svg></b><div style="font-size:4.6px;line-height:1.8;padding-top:2px"><b class="h" style="font-size:5px">ADDRESS:</b><br>120 Harbor Way, Suite 40<br>Fairview, GA 30100</div></div>
    <div style="display:flex;gap:10px;height:39px"><b style="flex:none;width:31px;height:31px;border-radius:50%;background:var(--navy);display:flex;align-items:center;justify-content:center"><svg width="13" height="13" style="color:#fff"><use href="#i-phone"/></svg></b><div style="font-size:4.6px;line-height:1.8;padding-top:6px"><b class="h" style="font-size:5px">PHONE:</b><br>555-014-2288</div></div>
    <div style="display:flex;gap:10px;height:39px"><b style="flex:none;width:31px;height:31px;border-radius:50%;background:var(--navy);display:flex;align-items:center;justify-content:center"><svg width="13" height="13" style="color:#fff"><use href="#i-mail"/></svg></b><div style="font-size:4.6px;line-height:1.8;padding-top:6px"><b class="h" style="font-size:5px">EMAIL:</b><br>hello@nexoratech.example</div></div>
  </div>

  <div class="field" style="left:193px;top:330px;width:107px;height:18px">First Name</div>
  <div class="field" style="left:304px;top:330px;width:107px;height:18px">Last Name</div>
  <div class="field" style="left:193px;top:354px;width:107px;height:18px">Phone Number</div>
  <div class="field" style="left:304px;top:354px;width:107px;height:18px">Email</div>
  <div class="field" style="left:193px;top:378px;width:218px;height:42px">Message</div>
  <div class="btn navy" style="left:193px;top:427px;width:61px;height:17px">SEND MESSAGE</div>

  <div class="footer" style="top:478px">
    <div class="flogo"><i></i>NEXORA TECH</div>
    <div class="fcol" style="left:168px"><h4>Quick Links</h4><ul><li>Home</li><li>About Us</li><li>Services</li><li>Contact Us</li></ul></div>
    <div class="fcol" style="left:237px"><h4>Other Links</h4><ul><li>FAQ</li><li>Terms of Use</li><li>Privacy Policy</li><li>Support Links</li><li>Conditions</li></ul></div>
    <div class="fcol fcontact" style="left:321px"><h4>Contact Us</h4><div><b><svg style="color:#fff"><use href="#i-pin"/></svg></b>Company Name,United State.</div><div><b><svg style="color:#fff"><use href="#i-mail"/></svg></b>info@companyname.com</div><div><b><svg style="color:#fff"><use href="#i-phone"/></svg></b>+1 555 010 0100</div></div>
    <hr><div class="copy">Copyrights@2025 Nexora Tech Services Group.All Rights Reserved</div>
  </div>
</div>

</div>
</body>
</html>
```